Pyramide TAGESFLUSS
Zielgruppe
Tobias Rahnfeld ist... Der Mann mit dem roten Stirnband (www.tobias-rahnfeld.com)
Videoinfo (BITTE UNBEDINGT ANSCHAUEN) unter:
http://www.clipvora.com/watch?v=pQ7mwe3tz8a
Er ist die Personifizierung eines eigenverantwortlichen und selbstbestimmten Lebens. Seit mehr als 15 Jahren beschäftigt er sich mit der Psychologie des Erfolgs und den Gesetzen des Lebens. Er entwickelte die Pyramide TAGESFLUSS und ist Urheber des Konzeptes SONNENKREIS WACHSEN.
Einzigartigkeit hat Tobias Rahnfeld schon früh erfahren. Im Alter von 16 war er nicht nur der jüngste Spieler in der Korbball-Oberklasse, sondern neun Jahre später auch einer der jüngsten Korbball-Oberklasse-Cheftrainer in der Geschichte dieses Sports. Er hat mit Jens Haverkamp zusammen gespielt, zwei Europameisterschaften für die deutsche Junioren-Nationalmannschaft absolviert und eine Europameisterschaft als Trainer gecoacht.
Parallel zu seiner Trainerkarriere hat Rahnfeld das BWL-Studium erfolgreich abgeschlossen. Darüber hinaus konnte er von Weltklasse-Nationaltrainern wie Uwe Leitgeber (Deutschland) oder Todd Wanamaker (USA) lernen, was Führungsstärke und -intelligenz bedeutet.
+++ Welche Produkte bieten wir an? -> Seminare, Vorträge und Bücher/Hörbücher +++
Tobias Rahnfeld steht für Erfolg, Glück und Erfüllung. Heute gibt er seine Expertise als gefragter Referent national und international an viele Menschen in Unternehmen aller Branchen weiter. Seine Seminarreihe SONNENKREIS WACHSEN mit den Events DER MUT, DEINEN WEG ZU GEHEN (www.tobias-rahnfeld.com/dermut), TATENDRANG Das Denken auf Ziele ausrichten (http://www.tobias-rahnfeld.com/events-tatendrang) und INNENSTÄRKE Freude und Sinn gestalten (www.tobias-rahnfeld.com/innenstaerke) hat sich in der Spitze der Persönlichkeitsentwicklung etabliert. Sie vermittelt Privatpersonen aller Altersklassen das Wissen, die mentalen Fähigkeiten und umsetzbaren Stra..
Aufgabenstellung
Es geht darum, die bereits bestehende Pyramide (zu sehen unter: http://www.tobias-rahnfeld.com/de/konzept) in eine neue "Form" zu bringen, die unserer gesamten CI/CD besser entspricht als die jetzige Variante. Sie muss/darf nicht wirklich ein Kunstwerk werden, sollte jedoch insgesamt dem Stil unseres Auftrittes entsprechen. Sie wird sowohl in Vorträgen und Seminaren an der Leinwand vor etlichen Leuten zu sehen sein, als auch auf der Website und in unseren Kommunikationsmaterialien Verwendung finden.
Zu den Reglern:
Modern - sie darf nicht zu modern sein, sollte jedoch auch nicht zu klassisch daher kommen. Die Zielgruppe sind Menschen von jung bis alt. Es geht hier nicht darum, eine spezielle Zielgruppe anzusprechen, sondern eher, eine einprägsame und schnell verständliche sowie übersichtliche Pyramide zu gestallten.
Exklusiv - kein Kommentar dazu. Eher im Mittelfeld.
Verspielt - weder noch. Zielgruppe ist weit gefasst, von daher muss auch die Pyramide vielen Menschen gefallen und sie muss ansprechend dargestellt werden.
Einfarbig: Es müssen die CI-Farben verwendet werden. Wichtig!
LAB: 38 63 37 - CMYK: 020 100 085 010 - RGB: 184 0 34 - HEX: B80022
Typo: Helvetica Neue LT Std

```html
<!DOCTYPE html>
<html lang="de">
<head>
<meta charset="utf-8">
<title>Pyramide TAGESFLUSS</title>
<link rel="stylesheet" href="https://fonts.googleapis.com/css2?family=Arimo:wght@400;700&display=swap">
<style>
  :root {
    --ci-red: #b80022;
    --paper: #ece8e1;
    --tier: #ffffff;
    --label-bg: #aca699;
    --label-text: #ffffff;
    --leader: #c9c4ba;
    --ink: #1a1a1a;
    --divider: #8f8a82;
  }
  * { margin: 0; padding: 0; box-sizing: border-box; }
  html, body { width: 1200px; height: 764px; overflow: hidden; background: var(--paper); }
  .canvas {
    position: relative;
    width: 1200px;
    height: 764px;
    background: var(--paper);
    font-family: "Arimo", "Helvetica Neue", Helvetica, Arial, sans-serif;
  }
  .pyramid { position: absolute; inset: 0; }
  .tier { fill: var(--tier); }
  .tier--apex { fill: var(--ci-red); }
  .leader { stroke: var(--leader); stroke-width: 1.5; }
  .level-tag { fill: var(--label-bg); }
  .level-name {
    fill: var(--label-text);
    font-size: 16px;
    letter-spacing: 0.3px;
    text-anchor: end;
  }
  .title {
    fill: var(--ci-red);
    font-size: 72px;
    font-weight: 400;
  }
  .row {
    position: absolute;
    left: 0;
    width: 1000px;
    display: flex;
    justify-content: center;
    align-items: center;
    transform: translateY(-50%);
  }
  .row__item {
    padding: 0 14px;
    font-size: 18px;
    font-weight: 700;
    color: var(--ink);
    text-align: center;
    line-height: 1.15;
    letter-spacing: 0.2px;
  }
  .row__item + .row__item { border-left: 1.5px solid var(--divider); }
  .row--mental .row__item { padding: 4px 12px; }
  .row--sense .row__item { color: #ffffff; }
</style>
</head>
<body>
<main class="canvas">
  <svg class="pyramid" width="1200" height="764" viewBox="0 0 1200 764" aria-hidden="true">
    <!-- leader lines -->
    <line class="leader" x1="500" y1="66" x2="574" y2="66"/>
    <line class="leader" x1="574.5" y1="159" x2="650" y2="159"/>
    <line class="leader" x1="646.7" y1="249" x2="714" y2="249"/>
    <line class="leader" x1="724.4" y1="346" x2="790" y2="346"/>
    <line class="leader" x1="798.2" y1="438" x2="867" y2="438"/>
    <line class="leader" x1="872.7" y1="531" x2="957" y2="531"/>

    <!-- tiers -->
    <polygon class="tier tier--apex" points="500,66 568.9,152 431.1,152"/>
    <polygon class="tier" points="425.5,159 574.5,159 641.1,242 358.9,242"/>
    <polygon class="tier" points="353.3,249 646.7,249 718.8,339 281.2,339"/>
    <polygon class="tier" points="275.6,346 724.4,346 792.6,431 207.4,431"/>
    <polygon class="tier" points="201.8,438 798.2,438 867.9,525 132.1,525"/>
    <polygon class="tier" points="127.3,531 872.7,531 942.5,618 57.5,618"/>

    <!-- level tags -->
    <rect class="level-tag" x="574" y="62" width="186" height="37"/>
    <text class="level-name" x="744" y="86">SINNEBENE</text>
    <rect class="level-tag" x="650" y="160" width="182" height="36"/>
    <text class="level-name" x="816" y="184">SOZIALEBENE</text>
    <rect class="level-tag" x="714" y="252" width="187" height="36"/>
    <text class="level-name" x="885" y="276">DEFINITIONSEBENE</text>
    <rect class="level-tag" x="790" y="345" width="188" height="36"/>
    <text class="level-name" x="962" y="369">WISSENSEBENE</text>
    <rect class="level-tag" x="867" y="438" width="187" height="36"/>
    <text class="level-name" x="1038" y="462">HANDLUNGSEBENE</text>
    <rect class="level-tag" x="957" y="530" width="187" height="36"/>
    <text class="level-name" x="1128" y="554">MENTALEBENE</text>

    <text class="title" x="112" y="698" textLength="773" lengthAdjust="spacingAndGlyphs">EIGENVERANTWORTUNG</text>
  </svg>

  <div class="row row--sense" style="top:123px"><span class="row__item">SINN</span></div>
  <div class="row row--social" style="top:210px">
    <span class="row__item">UMFELD</span><span class="row__item">UMGANG</span>
  </div>
  <div class="row row--definition" style="top:298px">
    <span class="row__item">WERTE</span><span class="row__item">SELBSTBILD</span><span class="row__item">REGELN</span>
  </div>
  <div class="row row--knowledge" style="top:390px">
    <span class="row__item">BERUF</span><span class="row__item">PARTNERSCHAFT</span><span class="row__item">GESUNDHEIT</span><span class="row__item">GELD</span>
  </div>
  <div class="row row--action" style="top:483px">
    <span class="row__item">DISZIPLIN</span><span class="row__item">PRIORITÄTEN</span><span class="row__item">ZIELE</span><span class="row__item">AUSDAUER</span><span class="row__item">NEUGIER</span>
  </div>
  <div class="row row--mental" style="top:574px">
    <span class="row__item">EMOTIONEN</span><span class="row__item">GEDANKEN</span><span class="row__item">SELBST-<br>VERTRAUEN</span><span class="row__item">ÜBER-<br>ZEUGUNGEN</span><span class="row__item">FOKUS</span><span class="row__item">SPIRITUALITÄT</span>
  </div>
</main>
</body>
</html>
```